CareVantRx business cards

We need a business card design that we could customize as needed for employees. We will need space for Name, Title, 1-2 phone numbers and email address.

We are a Pharmacy Benefits Management (PBM) company for hospice agencies and beginning a nationwide expansion. Attached is a vector file of our logo.

Cards can be single or double sided.

Industry/Entity Type

Business

```html
<!DOCTYPE html>
<html lang="en">
<head>
<meta charset="UTF-8">
<title>CareVantRx Business Cards</title>
<link href="https://fonts.googleapis.com/css2?family=Didact+Gothic&family=Questrial&display=swap" rel="stylesheet">
<style>
  :root {
    --backdrop: #2b2b2b;
    --card: #f7f7f5;
    --green: #8f9c4f;
    --blue: #3d75a2;
    --ink: #3a3a3a;
  }
  * { margin: 0; padding: 0; box-sizing: border-box; }
  html, body { width: 1200px; height: 900px; overflow: hidden; }
  body {
    position: relative;
    background: var(--backdrop);
    font-family: "Didact Gothic", "Questrial", sans-serif;
  }
  .card {
    position: absolute;
    left: 354px;
    width: 488px;
    height: 271px;
    background: var(--card);
    border-radius: 24px 0 24px 0;
    overflow: hidden;
  }
  .card--front { top: 157px; }
  .card--back { top: 466px; }

  .brand {
    position: absolute;
    display: flex;
    align-items: center;
    gap: 16px;
  }
  .brand__mark { background: var(--blue); border-radius: 6px; }
  .brand__name {
    font-family: "Questrial", sans-serif;
    color: var(--blue);
    line-height: 1;
    letter-spacing: -0.5px;
  }
  .card--front .brand { left: 35px; top: 102px; }
  .card--front .brand__mark { width: 68px; height: 68px; }
  .card--front .brand__name { font-size: 52px; }
  .card--back .brand { left: 74px; top: 37px; }
  .card--back .brand__mark { width: 60px; height: 60px; }
  .card--back .brand__name { font-size: 47px; }

  .band { position: absolute; bottom: 0; height: 16px; }
  .band--green { background: var(--green); }
  .band--blue { background: var(--blue); }
  .card--front .band--green { left: 0; width: 330px; }
  .card--front .band--blue { left: 338px; right: 0; }
  .card--back .band--blue { left: 0; width: 149px; }
  .card--back .band--green { left: 158px; right: 0; }

  .person {
    position: absolute;
    left: 147px;
    top: 152px;
    color: var(--ink);
    white-space: nowrap;
  }
  .person__name { font-size: 20px; }
  .person__title { font-size: 13px; text-transform: uppercase; margin-left: 4px; }
  .contact {
    position: absolute;
    left: 148px;
    top: 202px;
    font-size: 13px;
    line-height: 20px;
    color: var(--ink);
    white-space: nowrap;
  }
  .contact__label { color: var(--blue); margin-right: 6px; }
  .contact__gap { margin-left: 10px; }
</style>
</head>
<body>
  <section class="card card--front">
    <div class="brand">
      <span class="brand__mark"></span>
      <span class="brand__name">CareVantRx</span>
    </div>
    <span class="band band--green"></span>
    <span class="band band--blue"></span>
  </section>

  <section class="card card--back">
    <div class="brand">
      <span class="brand__mark"></span>
      <span class="brand__name">CareVantRx</span>
    </div>
    <p class="person">
      <span class="person__name">Dana Whitfield</span>
      <span class="person__title">Operation Manager</span>
    </p>
    <div class="contact">
      <p><span class="contact__label">T</span>(221) 33 412 76 58<span class="contact__label contact__gap">M</span>(221) 77 905 14 63</p>
      <p><span class="contact__label">E</span>dana@carevantrx.com</p>
    </div>
    <span class="band band--blue"></span>
    <span class="band band--green"></span>
  </section>
</body>
</html>
```